Small IT consulting firm needs a new web site

Quellmark Systems, LLC is a company based out of Arizona with national presence. We work on both national, multinational, and international projects. We are Brantova Partners. Heavy experience and work with Nodewell Control Suite, Velquo, Trellin 820 . We offer Architecture, Design, Development, and implementation services. We have a specialty in Trellin 820 migrations and implementations. We also have a specialized practice in Program and Project Management. The design message should foster a feeling of partnership and experience. Attached is my logo.
Industry/Entity Type
It Company
Coding
Coded - Design and coding required
Number of Pages Required
5+ page
Look and feel

```html
<!DOCTYPE html>
<html lang="en">
<head>
<meta charset="utf-8">
<title>Quellmark Systems, LLC</title>
<link href="https://fonts.googleapis.com/css2?family=Raleway:wght@400;500;600;700&family=Cinzel:wght@500&display=swap" rel="stylesheet">
<style>
:root{
  --red:#c8202a;
  --red-dark:#a5161f;
  --ink:#2b2b2b;
  --text:#555;
  --muted:#8a8a8a;
  --light:#f4f4f4;
  --band:#ededed;
  --rule:#cfcfcf;
  --nav-top:#8a8a8a;
  --nav-bottom:#3f3f3f;
  --footer:#2e2e2e;
  --teal-a:#0f5f7a;
  --teal-b:#3fa3c2;
  --white:#fff;
}
*{box-sizing:border-box;margin:0;padding:0}
html,body{width:1200px;height:2314px;overflow:hidden}
body{font-family:"Raleway",Arial,sans-serif;color:var(--text);background:var(--white);position:relative}
.abs{position:absolute}

/* header */
.site-header{position:absolute;left:0;top:0;width:1200px;height:123px;background:linear-gradient(#ffffff,#eeeeee)}
.brand{position:absolute;left:86px;top:26px;display:flex;align-items:center;gap:14px}
.brand-mark{width:48px;height:48px;background:var(--red)}
.brand-name{font-size:30px;font-weight:700;color:var(--red);letter-spacing:.5px}
.top-contact{position:absolute;top:24px;right:86px;display:flex;gap:38px;font-size:21px;color:#666}
.top-contact span{display:flex;align-items:center;gap:10px}
.main-nav{position:absolute;left:447px;top:77px;width:753px;height:46px;background:linear-gradient(var(--nav-top),var(--nav-bottom));clip-path:polygon(18px 0,100% 0,100% 100%,0 100%)}
.main-nav a{position:absolute;top:13px;transform:translateX(-50%);font-size:14px;font-weight:700;color:#fff;text-decoration:none;letter-spacing:.5px}
.main-nav a.active{top:9px;background:var(--red);padding:4px 10px}
.main-nav i{position:absolute;top:0;width:1px;height:46px;background:rgba(255,255,255,.25)}

/* hero */
.hero{position:absolute;left:0;top:123px;width:1200px;height:514px;background:radial-gradient(circle at 30% 45%,#9fd8ea 0%,var(--teal-b) 30%,var(--teal-a) 100%)}
.hero-card{position:absolute;left:734px;top:70px;width:382px;height:382px;border-radius:50%;background:rgba(255,255,255,.9);text-align:center;padding-top:104px}
.hero-title{font-family:"Cinzel",Georgia,serif;font-size:28px;line-height:32px;color:#333;letter-spacing:1px}
.hero-text{font-size:17px;line-height:26px;color:#444;margin:14px auto 0;width:330px}
.btn{display:inline-block;background:var(--red);color:#fff;font-weight:700;text-decoration:none}
.hero-card .btn{margin-top:14px;font-size:16px;padding:10px 26px}
.dots{margin-top:20px;display:flex;justify-content:center;gap:10px}
.dots b{width:14px;height:14px;border-radius:50%;background:#333}
.dots b.on{background:#fff;border:2px solid var(--red)}

/* section headings */
.section-title{position:absolute;left:0;width:1200px;text-align:center;font-size:28px;font-weight:600;color:var(--ink);letter-spacing:.3px}
.section-title em{font-style:normal;color:var(--red)}
.divider{position:absolute;left:327px;width:546px;height:12px}

/* welcome */
.welcome-lead{position:absolute;left:86px;top:755px;width:1028px;text-align:center;font-size:22px;color:#555}
.welcome-body{position:absolute;left:86px;top:802px;width:1028px;text-align:center;font-size:13px;line-height:24px;color:#555}
.welcome .btn{position:absolute;left:535px;top:899px;width:128px;height:32px;line-height:32px;text-align:center;font-size:14px}

/* services */
.services{position:absolute;left:0;top:981px;width:1200px;height:425px;background:var(--band)}
.service{position:absolute;top:188px;width:242px;height:206px}
.service-photo{position:absolute;inset:0;background:linear-gradient(135deg,#6b6b6b,#4a4a4a)}
.service h3{position:absolute;top:62px;width:100%;text-align:center;font-size:21px;font-weight:600;color:#fff}
.service p{position:absolute;top:102px;left:14px;right:14px;text-align:center;font-size:13px;line-height:19px;color:#eee}
.service-plus{position:absolute;left:103px;bottom:0;width:36px;height:14px;background:var(--red);clip-path:polygon(50% 0,100% 100%,0 100%)}
.service-plus::after{content:"+";position:absolute;left:0;right:0;top:-3px;text-align:center;color:#fff;font-size:15px;font-weight:700}
.service-badge{position:absolute;top:-64px;left:52px;width:138px;height:138px}

/* specialize */
.specialize{position:absolute;left:0;top:1406px;width:1200px;height:571px;background:#fafafa}
.spec-item{position:absolute;left:86px;width:562px}
.spec-item .icon{position:absolute;left:0;top:-6px;width:80px;height:80px;border-radius:50%;background:#fff;border:1px solid #e2e2e2}
.spec-item h4{position:absolute;left:94px;top:0;font-size:19px;font-weight:600;color:#444}
.spec-item p{position:absolute;left:94px;top:32px;width:468px;font-size:13px;line-height:20px;color:#666}
.spec-rule{position:absolute;left:86px;width:562px;height:1px;background:#e2e2e2}
.video{position:absolute;left:683px;top:119px;width:431px;height:393px;background:#222}
.video-frame{position:absolute;left:0;top:0;width:431px;height:360px;background:radial-gradient(circle at 40% 50%,#bfe6f1,#4f9fba 55%,#2a6e88)}
.video-controls{position:absolute;left:0;bottom:0;width:431px;height:33px;background:#1c1c1c}

/* clients */
.clients{position:absolute;left:0;top:1977px;width:1200px;height:120px;background:var(--band)}
.clients h2{position:absolute;left:86px;top:25px;font-size:30px;line-height:33px;font-weight:600;color:var(--ink)}
.clients h2 em{font-style:normal;color:var(--red)}
.client{position:absolute;top:27px;height:67px;background:#fff;border:1px solid #ddd;display:flex;align-items:center;justify-content:center;gap:6px;font-size:14px;font-weight:700;color:#444;text-align:center;line-height:16px}
.client i{width:12px;height:12px;background:var(--red);flex:none}
.arrow{position:absolute;top:46px;font-size:26px;color:#bbb}

/* footer */
.site-footer{position:absolute;left:0;top:2097px;width:1200px;height:170px;background:var(--footer);color:#fff}
.footer-nav{position:absolute;left:86px;top:14px;display:flex;align-items:center;gap:16px;font-size:13px;font-weight:700}
.footer-nav svg{flex:none}
.footer-rule{position:absolute;left:86px;top:46px;width:767px;height:1px;background:#555}
.address{position:absolute;left:86px;top:68px;font-size:13px;line-height:21px;font-style:normal}
.contact-list{position:absolute;left:375px;top:68px;font-size:13px;line-height:29px}
.contact-list div{display:flex;align-items:center;gap:10px}
.subscribe-input{position:absolute;left:621px;top:66px;width:232px;height:34px;background:#fff;color:#777;font-size:13px;padding:9px 12px}
.subscribe-btn{position:absolute;left:621px;top:111px;width:232px;height:34px;background:var(--red);border:1px solid #e05a60;color:#fff;font-size:13px;font-weight:700;text-align:center;line-height:32px}
.footer-brand{position:absolute;left:880px;top:88px;width:234px;text-align:right;font-size:20px;font-weight:700;color:#555;white-space:nowrap}
.bottom-bar{position:absolute;left:0;top:2267px;width:1200px;height:47px;background:var(--red);color:#fff}
.copyright{position:absolute;left:86px;top:16px;font-size:13px;font-weight:600}
.social{position:absolute;top:10px;width:28px;height:28px;border-radius:50%;background:#fff}
</style>
</head>
<body>

<header class="site-header">
  <div class="brand"><div class="brand-mark"></div><div class="brand-name">Quellmark Systems, LLC</div></div>
  <div class="top-contact">
    <span><svg width="26" height="26" viewBox="0 0 26 26"><circle cx="13" cy="13" r="11.5" fill="none" stroke="#c8202a" stroke-width="2"/><path d="M9 7l3 3-1.6 1.8c.8 1.8 2 3 3.8 3.8L16 14l3 3-2 2c-4.5-.5-8.5-4.5-9-9z" fill="#c8202a"/></svg>555-014-2290</span>
    <span><svg width="24" height="18" viewBox="0 0 24 18"><rect x="1" y="1" width="22" height="16" rx="2" fill="#c8202a"/><path d="M2 3l10 7 10-7" fill="none" stroke="#fff" stroke-width="2"/></svg>info@quellmark.com</span>
  </div>
  <nav class="main-nav">
    <a class="active" style="left:39px">HOME</a>
    <i style="left:118px"></i>
    <a style="left:164px">ABOUT</a>
    <i style="left:230px"></i>
    <a style="left:299px">SERVICES</a>
    <i style="left:380px"></i>
    <a style="left:464px">TESTIMONIALS</a>
    <i style="left:560px"></i>
    <a style="left:629px">CONTACT</a>
  </nav>
</header>

<section class="hero" role="img" aria-label="Photo of a hand touching a glowing circuit board">
  <div class="hero-card">
    <div class="hero-title">Lorem ipsum dol<br>sit amet adipiscing</div>
    <p class="hero-text">Lorem ipsum dolor sit amet, consectetur eleifend eros lacus, sed convallis augue</p>
    <a class="btn">Learn More</a>
    <div class="dots"><b></b><b class="on"></b><b></b><b></b></div>
  </div>
</section>

<section class="welcome">
  <h1 class="section-title" style="top:680px"><em>WELCOME TO</em> QUELLMARK SYSTEMS LLC</h1>
  <svg class="divider" style="top:713px" viewBox="0 0 546 12"><path d="M0 4h261M0 8h261M285 4h261M285 8h261" stroke="#bbb"/><rect x="267" y="0" width="8.5" height="8.5" transform="rotate(45 273 6)" fill="#fff" stroke="#999"/></svg>
  <p class="welcome-lead">Duis autem vel eum iriure dolor in hendrerit in vulputate velit esse molestie consequat, velillum</p>
  <p class="welcome-body">Lorem ipsum dolor sit amet, consectetuer adipiscing elit, sed diam nonummy nibh euismod tincidunt ut laoreet dolore magna aliquam erat volutpat. Ut wisi enim minim veniam, quis nostrud exerci tation ullamcorper suscipit lobortis nisl ut aliquip ex ea commodo consequat. Dolore eu feugiat nulla facilisis at vero eros et accumsan et iusto odio dignissim qui blandit praesent luptatum zzril delenit augue duis dolore te feugait nulla facilisi.</p>
  <a class="btn">LEARN MORE</a>
</section>

<section class="services">
  <h2 class="section-title" style="top:20px"><em>OUR</em> SERVICES</h2>
  <svg class="divider" style="top:60px" viewBox="0 0 546 12"><path d="M0 4h261M0 8h261M285 4h261M285 8h261" stroke="#bbb"/><rect x="267" y="0" width="8.5" height="8.5" transform="rotate(45 273 6)" fill="#ededed" stroke="#999"/></svg>

  <div class="service" style="left:86px">
    <div class="service-photo" role="img" aria-label="Photo of architectural blueprints"></div>
    <svg class="service-badge" viewBox="0 0 138 138"><rect x="20" y="20" width="98" height="98" transform="rotate(45 69 69)" fill="#c8202a"/><circle cx="69" cy="69" r="40" fill="#fff"/><path d="M50 70l14-12 14 12v14H50z" fill="none" stroke="#333" stroke-width="3"/><rect x="60" y="72" width="8" height="12" fill="#333"/><path d="M76 88l14-22 4 3-14 22-5 2z" fill="#333"/></svg>
    <h3>Architecture</h3>
    <p>Ut wisi enim ad minim veniam, quis nostrud exerci lobortis nisl ut aliquip ex ea commodo.</p>
    <div class="service-plus"></div>
  </div>
  <div class="service" style="left:348px">
    <div class="service-photo" role="img" aria-label="Photo of colourful paint swatches" style="background:linear-gradient(135deg,#7a6a5a,#5a5f6a 50%,#6b5e4e)"></div>
    <svg class="service-badge" viewBox="0 0 138 138"><rect x="20" y="20" width="98" height="98" transform="rotate(45 69 69)" fill="#c8202a"/><circle cx="69" cy="69" r="40" fill="#fff"/><ellipse cx="66" cy="71" rx="19" ry="16" fill="#333"/><circle cx="58" cy="65" r="3" fill="#fff"/><circle cx="66" cy="61" r="3" fill="#fff"/><circle cx="74" cy="65" r="3" fill="#fff"/><circle cx="60" cy="77" r="3.5" fill="#fff"/><path d="M76 82l12-22 3 2-10 22z" fill="#333"/></svg>
    <h3>Design</h3>
    <p>Ut wisi enim ad minim veniam, quis nostrud exerci lobortis nisl ut aliquip ex ea commodo.</p>
    <div class="service-plus"></div>
  </div>
  <div class="service" style="left:610px">
    <div class="service-photo" role="img" aria-label="Photo of puzzle pieces"></div>
    <svg class="service-badge" viewBox="0 0 138 138"><rect x="20" y="20" width="98" height="98" transform="rotate(45 69 69)" fill="#c8202a"/><circle cx="69" cy="69" r="40" fill="#fff"/><rect x="49" y="54" width="40" height="28" rx="2" fill="none" stroke="#333" stroke-width="3"/><path d="M63 86h12M69 82v4" stroke="#333" stroke-width="3"/><path d="M62 63l-5 5 5 5M76 63l5 5-5 5M71 61l-4 14" fill="none" stroke="#333" stroke-width="2"/></svg>
    <h3>Development</h3>
    <p>Ut wisi enim ad minim veniam, quis nostrud exerci lobortis nisl ut aliquip ex ea commodo.</p>
    <div class="service-plus"></div>
  </div>
  <div class="service" style="left:872px">
    <div class="service-photo" role="img" aria-label="Photo of white puzzle pieces"></div>
    <svg class="service-badge" viewBox="0 0 138 138"><rect x="20" y="20" width="98" height="98" transform="rotate(45 69 69)" fill="#c8202a"/><circle cx="69" cy="69" r="40" fill="#fff"/><circle cx="61" cy="75" r="12" fill="none" stroke="#333" stroke-width="7" stroke-dasharray="5 3"/><circle cx="61" cy="75" r="4" fill="#333"/><circle cx="79" cy="60" r="8" fill="none" stroke="#333" stroke-width="5" stroke-dasharray="4 2.5"/><circle cx="79" cy="60" r="2.5" fill="#333"/></svg>
    <h3>Implementation</h3>
    <p>Ut wisi enim ad minim veniam, quis nostrud exerci lobortis nisl ut aliquip ex ea commodo.</p>
    <div class="service-plus"></div>
  </div>
</section>

<section class="specialize">
  <h2 class="section-title" style="top:28px"><em>WE</em> SPECIALIZE IN</h2>
  <svg class="divider" style="top:65px" viewBox="0 0 546 12"><path d="M0 4h261M0 8h261M285 4h261M285 8h261" stroke="#bbb"/><rect x="267" y="0" width="8.5" height="8.5" transform="rotate(45 273 6)" fill="#fafafa" stroke="#999"/></svg>

  <div class="spec-item" style="top:124px">
    <div class="icon"><svg width="80" height="80" viewBox="0 0 80 80"><path d="M40 24l16 8-16 8-16-8z" fill="#c8202a"/><path d="M24 40l16 8 16-8M24 48l16 8 16-8" fill="none" stroke="#c8202a" stroke-width="3" stroke-linejoin="round"/></svg></div>
    <h4>Trellin 820</h4>
    <p>Ut wisi enim minim veniam, quis nostrud exerci tation ullamcorper norl suscipit lobortis nisl ut aliquip ex ea commodo consequat.</p>
  </div>
  <div class="spec-rule" style="top:210px"></div>
  <div class="spec-item" style="top:228px">
    <div class="icon"><svg width="80" height="80" viewBox="0 0 80 80"><path d="M30 52a9 9 0 0 1 0-18 12 12 0 0 1 23-2 10 10 0 0 1 0 20z" fill="#c8202a"/></svg></div>
    <h4>Velquo</h4>
    <p>Ut wisi enim minim veniam, quis nostrud exerci tation ullamcorper norl suscipit lobortis nisl ut aliquip ex ea commodo consequat.</p>
  </div>
  <div class="spec-rule" style="top:314px"></div>
  <div class="spec-item" style="top:331px">
    <div class="icon"><svg width="80" height="80" viewBox="0 0 80 80"><path d="M38 24l16 16-16 16" fill="none" stroke="#c8202a" stroke-width="4"/><path d="M24 40h28" stroke="#c8202a" stroke-width="4"/><path d="M24 30v20" stroke="#c8202a" stroke-width="4"/></svg></div>
    <h4>Program</h4>
    <p>Ut wisi enim minim veniam, quis nostrud exerci tation ullamcorper norl suscipit lobortis nisl ut aliquip ex ea commodo consequat.</p>
  </div>
  <div class="spec-item" style="top:454px">
    <div class="icon"><svg width="80" height="80" viewBox="0 0 80 80"><rect x="24" y="26" width="20" height="7" fill="#c8202a"/><rect x="34" y="37" width="22" height="7" fill="#c8202a"/><rect x="28" y="48" width="26" height="7" fill="#c8202a"/><path d="M24 24v34h32" fill="none" stroke="#c8202a" stroke-width="2"/></svg></div>
    <h4>Project Management</h4>
    <p>Ut wisi enim minim veniam, quis nostrud exerci tation ullamcorper norl suscipit lobortis nisl ut aliquip ex ea commodo consequat.</p>
  </div>

  <div class="video">
    <div class="video-frame" role="img" aria-label="Video still of a hand touching a circuit board"></div>
    <svg class="abs" style="left:183px;top:155px" width="66" height="50" viewBox="0 0 66 50"><circle cx="33" cy="25" r="25" fill="#c8202a"/><path d="M26 15l18 10-18 10z" fill="#fff"/></svg>
    <div class="video-controls">
      <svg width="431" height="33" viewBox="0 0 431 33"><rect x="14" y="11" width="3" height="11" fill="#fff"/><rect x="20" y="11" width="3" height="11" fill="#fff"/><rect x="34" y="15" width="275" height="3" fill="#555"/><rect x="34" y="15" width="140" height="3" fill="#c8202a"/><circle cx="174" cy="16.5" r="5" fill="#fff"/><path d="M334 11h10M334 15h10M334 19h10M334 23h10" stroke="#999"/><rect x="368" y="13" width="48" height="7" rx="3.5" fill="#444"/><circle cx="392" cy="16.5" r="8" fill="#ddd"/></svg>
    </div>
  </div>
</section>

<section class="clients">
  <h2><em>Our</em><br>Clients</h2>
  <span class="arrow" style="left:245px">&lsaquo;</span>
  <div class="client" style="left:276px;width:151px"><i></i>Harlow Ferro Bank</div>
  <div class="client" style="left:446px;width:166px"><i></i>Dunmere Controls</div>
  <div class="client" style="left:631px;width:179px"><i></i>Peregal Financial</div>
  <div class="client" style="left:828px;width:114px">Castwell<br>Automation</div>
  <div class="client" style="left:961px;width:123px">Marrick</div>
  <span class="arrow" style="left:1101px">&rsaquo;</span>
</section>

<footer class="site-footer">
  <div class="footer-nav">
    <span>Home</span><svg width="10" height="10"><rect x="2" y="2" width="6" height="6" transform="rotate(45 5 5)" fill="none" stroke="#888"/></svg>
    <span>About</span><svg width="10" height="10"><rect x="2" y="2" width="6" height="6" transform="rotate(45 5 5)" fill="none" stroke="#888"/></svg>
    <span>Services</span><svg width="10" height="10"><rect x="2" y="2" width="6" height="6" transform="rotate(45 5 5)" fill="none" stroke="#888"/></svg>
    <span>Testimonials</span><svg width="10" height="10"><rect x="2" y="2" width="6" height="6" transform="rotate(45 5 5)" fill="none" stroke="#888"/></svg>
    <span>Contact</span>
  </div>
  <div class="footer-rule"></div>
  <address class="address">Quellmark Systems LLC<br>1187 W Corvin Road<br>Suite 220-415<br>Tempe, AZ 85281</address>
  <div class="contact-list">
    <div><svg width="14" height="14" viewBox="0 0 14 14"><path d="M2 1l3 3-1.5 1.8c.8 1.8 2 3 3.8 3.8L9 8l3 3-2 2C5.5 12.5 1.5 8.5 1 4z" fill="#fff"/></svg>555-014-2290</div>
    <div><svg width="14" height="14" viewBox="0 0 14 14"><path d="M2 1l3 3-1.5 1.8c.8 1.8 2 3 3.8 3.8L9 8l3 3-2 2C5.5 12.5 1.5 8.5 1 4z" fill="#fff"/></svg>555-014-2290</div>
    <div><svg width="14" height="11" viewBox="0 0 14 11"><rect width="14" height="11" fill="#fff"/><path d="M1 1l6 5 6-5" fill="none" stroke="#2e2e2e" stroke-width="1.5"/></svg>info@quellmark.com</div>
  </div>
  <div class="subscribe-input">Enter Your Email Here</div>
  <div class="subscribe-btn">SUBMIT</div>
  <div class="footer-brand">Quellmark Systems, LLC</div>
</footer>

<div class="bottom-bar">
  <p class="copyright">© 2015 Quellmarksystemsllc. All Rights Reserved</p>
  <span class="social" style="left:973px" aria-label="Social link"></span>
  <span class="social" style="left:1011px" aria-label="Social link"></span>
  <span class="social" style="left:1050px" aria-label="Social link"></span>
  <span class="social" style="left:1086px" aria-label="Social link"></span>
</div>

</body>
</html>
```